Website for data analytics startup

I have a landing page up at http://vimero.io I need to expand this into a basic company website. I want something similar to this design: http://gridkitly.com/examples/slider/

I need HTML and CSS for each of the designs, once they are approved. I need the following pages: home page, product, team, blog, and a design for the container of our demo application.

Our logo is attached and also available here: https://files.cloudvaultix.net/vimero.public/LOGO-colour.png I would like the website branding to match the logo.

I need a blog design with CSS that works with Tumblr.

Our app can be seen at http://demo.vimero.io Please don't change the look of the network graph itself, only the surrounding content.

For CSS, I want you to use Bootstrap or Foundation as the starting point.

Target Market(s)

Sales and marketing, strategy

Industry/Entity Type

It Company

Coding

Coded - Design and coding required

Number of Pages Required

4 page

Font styles to use
Serif
Sans Serif

Requirements
Must have
• Clean, healthy appeal. Must work well with our logo. Blog page must integrate with Tumblr easily. Must use Bootstrap or Foundation for the starting point of the HTML/CSS.
Should not have
• Ugly crap, flash looking design. NO FLASH.

```html
<!DOCTYPE html>
<html lang="en">
<head>
<meta charset="utf-8">
<title>Vimero</title>
<link rel="stylesheet" href="https://fonts.googleapis.com/css2?family=Questrial&family=Arimo:wght@400;700&display=swap">
<style>
:root{
  --green:#8cc63f;
  --green-dark:#76b82a;
  --sky:#5bc0eb;
  --navy:#0d1b2a;
  --logo-navy:#1d4a6b;
  --ink:#444;
  --muted:#777;
  --line:#e4e4e4;
  --pale:#f6f6f6;
  --white:#fff;
}
*{box-sizing:border-box;margin:0;padding:0}
html,body{width:924px;height:1200px;overflow:hidden;background:var(--white)}
body{position:relative;font-family:"Questrial",sans-serif;color:var(--ink)}
.abs{position:absolute}

.top-rule{left:0;top:0;width:924px;height:2px;background:var(--sky)}
.site-header{left:0;top:2px;width:924px;height:79px;background:var(--white)}
.brand{left:76px;top:20px;display:flex;align-items:center;gap:8px}
.brand-dot{width:12px;height:12px;border-radius:50%;background:var(--green)}
.brand-name{font-size:30px;color:var(--logo-navy);letter-spacing:.5px}
.main-nav a{position:absolute;top:28px;height:24px;line-height:24px;font-size:10.5px;color:#444;text-decoration:none;font-family:"Arimo",sans-serif}
.main-nav .is-active{left:475px;width:53px;text-align:center;background:var(--green);color:var(--white)}

.hero{left:0;top:81px;width:924px;height:328px;
  background:radial-gradient(ellipse at 8% 25%,rgba(120,160,200,.45),transparent 30%),
             radial-gradient(ellipse at 55% 40%,#1d5a8c 0%,#0c3a63 45%,#062540 100%);
  text-align:center;color:var(--white)}
.hero-title{position:absolute;left:0;right:0;top:110px;font-size:42px;font-weight:400;text-shadow:0 2px 4px rgba(0,0,0,.35)}
.hero-lead{position:absolute;left:0;right:0;top:156px;font-size:13px;line-height:21px}
.hero-arrows{position:absolute;left:424px;top:231px}

.signup-band{left:0;top:409px;width:924px;height:134px;
  background:linear-gradient(120deg,#8ac44a 0%,#93ca55 55%,#a2d46a 80%,#8cc63f 100%)}
.signup-title{position:absolute;left:76px;top:13px;font-size:19px;color:var(--white);font-weight:400}
.signup-note{position:absolute;left:76px;top:39px;font-size:10.5px;color:var(--white)}
.field{position:absolute;top:74px;height:27px;border:1px solid rgba(255,255,255,.85);color:var(--white);font-size:10.5px;line-height:25px;padding-left:9px}
.callback{position:absolute;left:714px;top:72px;width:132px;height:32px;background:var(--sky);color:var(--white);font-size:11px;line-height:32px;text-align:center}

.feature{top:582px;width:262px;text-align:center}
.feature-icon{display:block;margin:0 auto}
.feature-title{margin-top:12px;font-size:16.5px;font-weight:400;color:#555}
.feature-text{margin-top:12px;font-family:"Arimo",sans-serif;font-size:8.3px;line-height:15.3px;color:var(--muted);padding:0 16px}
.divider{top:602px;width:1px;height:172px;background:var(--line)}

.about{left:0;top:806px;width:924px;height:273px;background:var(--pale)}
.about-visual{position:absolute;left:82px;top:20px;width:246px;height:236px;border-radius:6px;
  background:linear-gradient(180deg,#2b2b2b 0%,#3a3a3a 58%,#d9d9d9 62%,#eeeeee 100%)}
.about-title{position:absolute;left:347px;top:28px;font-size:17px;font-weight:400;color:#555}
.about-title span{color:var(--green)}
.about-text{position:absolute;left:347px;width:500px;font-family:"Arimo",sans-serif;font-size:8.1px;line-height:15.9px;color:var(--muted)}
.demo-btn{position:absolute;left:347px;top:224px;width:181px;height:30px;background:var(--green);color:var(--white);font-size:11px;line-height:30px;text-align:center}

.site-footer{left:0;top:1079px;width:924px;height:121px;background:var(--navy);color:var(--white);text-align:center}
.social{position:absolute;left:394px;top:18px}
.footer-nav{position:absolute;left:0;right:0;top:61px;font-family:"Arimo",sans-serif;font-size:8.8px;word-spacing:1px}
.footer-nav span{margin:0 12px}
.copyright{position:absolute;left:0;right:0;top:88px;font-family:"Arimo",sans-serif;font-size:8.5px}
</style>
</head>
<body>
<div class="abs top-rule"></div>

<header class="abs site-header">
  <div class="abs brand"><span class="brand-dot"></span><span class="brand-name">vimero</span></div>
  <nav class="main-nav">
    <a class="is-active">HOME</a>
    <a style="left:554px">ABOUT US</a>
    <a style="left:640px">SERVICES</a>
    <a style="left:722px">NEWS</a>
    <a style="left:789px">CONTACT US</a>
  </nav>
</header>

<section class="abs hero" role="img" aria-label="Glowing blue network of light trails">
  <h1 class="hero-title">Welcome to Vimero</h1>
  <p class="hero-lead">It is a long established fact that a reader will be distracted by the readable content of a page when<br>Lorem Ipsum is that it content here', making it look like readable English.</p>
  <svg class="hero-arrows" width="76" height="36" viewBox="0 0 76 36" fill="none" stroke="#dfe9f2" stroke-width="2">
    <circle cx="17" cy="17" r="16"/><path d="M20 10l-7 7 7 7"/>
    <circle cx="57" cy="17" r="16"/><path d="M54 10l7 7-7 7"/>
  </svg>
</section>

<section class="abs signup-band">
  <h2 class="signup-title">Get Started Now</h2>
  <p class="signup-note">As soon as you contact our expert team, this will be the only form you have to fill in!</p>
  <div class="field" style="left:76px;width:123px">Name* :</div>
  <div class="field" style="left:208px;width:124px">Email* :</div>
  <div class="field" style="left:342px;width:124px">Phone* :</div>
  <div class="field" style="left:475px;width:219px">Messages* :</div>
  <div class="callback">REQUEST A CALLBACK</div>
</section>

<article class="abs feature" style="left:63px">
  <svg class="feature-icon" width="92" height="92" viewBox="0 0 92 92">
    <circle cx="46" cy="46" r="45" fill="var(--sky)" stroke="#4aa9d6" stroke-width="1.5"/>
    <rect x="30" y="32" width="32" height="21" rx="2" fill="none" stroke="#fff" stroke-width="3"/>
    <path d="M24 57h44l-3 4H27z" fill="#fff"/>
  </svg>
  <h3 class="feature-title">Contrary to Popular</h3>
  <p class="feature-text">It is a long established fact that a reader will be distracted by the of letters, as opposed to using 'Content here, content here making it look like readable English.</p>
</article>
<div class="abs divider" style="left:326px"></div>
<article class="abs feature" style="left:331px">
  <svg class="feature-icon" width="92" height="92" viewBox="0 0 92 92">
    <circle cx="46" cy="46" r="45" fill="var(--sky)" stroke="#4aa9d6" stroke-width="1.5"/>
    <g fill="#fff"><ellipse cx="46" cy="31" rx="18" ry="6"/>
    <path d="M28 36c0 3 8 6 18 6s18-3 18-6v6c0 3-8 6-18 6s-18-3-18-6z"/>
    <path d="M28 47c0 3 8 6 18 6s18-3 18-6v6c0 3-8 6-18 6s-18-3-18-6z"/>
    <path d="M28 58c0 3 8 6 18 6s18-3 18-6v4c0 3-8 6-18 6s-18-3-18-6z"/></g>
  </svg>
  <h3 class="feature-title">Contrary to Popular</h3>
  <p class="feature-text">It is a long established fact that a reader will be distracted by the of letters, as opposed to using 'Content here, content here making it look like readable English.</p>
</article>
<div class="abs divider" style="left:596px"></div>
<article class="abs feature" style="left:595px">
  <svg class="feature-icon" width="92" height="92" viewBox="0 0 92 92">
    <circle cx="46" cy="46" r="45" fill="var(--sky)" stroke="#4aa9d6" stroke-width="1.5"/>
    <g fill="#fff"><path d="M27 27h3v34h36v3H27z"/>
    <rect x="34" y="44" width="5" height="15"/><rect x="42" y="38" width="5" height="21"/>
    <rect x="50" y="47" width="5" height="12"/><rect x="58" y="34" width="5" height="25"/></g>
  </svg>
  <h3 class="feature-title">Contrary to Popular</h3>
  <p class="feature-text">It is a long established fact that a reader will be distracted by the of letters, as opposed to using 'Content here, content here making it look like readable English.</p>
</article>

<section class="abs about">
  <div class="about-visual" role="img" aria-label="Desktop computer showing a market network graph"></div>
  <h2 class="about-title">Vimero Maps Markets to <span>Drive Sales and Marketing</span></h2>
  <p class="about-text" style="top:82px">It is a long established fact that a reader will be distracted by the readable content of a page when looking at its layout. The point of using Lorem Ipsum is that it has a more-or-less normal distribution of letters, as opposed to using 'Content here, content here', making it look like readable English. Many desktop publishing packages and web Contrary to popular belief, Lorem Ipsum is not simply random text. It has roots in a piece of classical Latin literature from page editors now use Lorem Ipsum as their default model text, and a search for 'lorem ipsum' will uncover many web sites still in their infancy.....</p>
  <p class="about-text" style="top:160px">Many desktop publishing packages and web Contrary to popular belief, Lorem Ipsum is not simply random text. It has roots in a piece of classical Latin literature from page editors now use Lorem Ipsum as their default model text, and a search for 'lorem ipsum' will uncover many web sites still in their infancy.....</p>
  <div class="demo-btn">SIGN UP NOW FOR A FREE DEMO</div>
</section>

<footer class="abs site-footer">
  <svg class="social" width="136" height="28" viewBox="0 0 136 28" fill="none" stroke="#fff" stroke-width="1.2" role="img" aria-label="Social network links">
    <circle cx="14" cy="14" r="13"/><circle cx="50" cy="14" r="13"/><circle cx="86" cy="14" r="13"/><circle cx="122" cy="14" r="13"/>
  </svg>
  <p class="footer-nav">HOME<span>|</span>ABOUT US<span>|</span>SERVICES<span>|</span>NEWS<span>|</span>CONTACT US</p>
  <p class="copyright">©&nbsp; Copyright2015 Vimero All rights reserved.</p>
</footer>
</body>
</html>
```